Healthcare IT firm needs classy and unique business care design

We need a business card design that incorporates our new logo design (attached) Prefer a purple based designed. I would really love to see something utilizing the "3D" version of the logo (purple on the reflective wall). I want something a little more than my logo printed along with a person's detailed contact information.
Contact Information for Business Card
Want something polished, professional, and a little unique in the design.
Colors
6b449b
Requirements
Must have
- Please use similar font as the logo design
Nice to have
- Would like to see the 3d version of my logo incorporated into the design.

```html
<!DOCTYPE html>
<html lang="en">
<head>
<meta charset="utf-8">
<title>Meridel Health Systems — Business Card</title>
<link rel="stylesheet" href="https://fonts.googleapis.com/css2?family=Arimo:wght@400;700&family=Montserrat:wght@600&display=swap">
<style>
  :root {
    --page-bg: #e9e6ee;
    --brand: #6b449b;
    --brand-deep: #3b2468;
    --brand-mid: #5a3a8e;
    --card-white: #ffffff;
    --ink: #333333;
    --on-brand: #ffffff;
    --shadow: rgba(40, 20, 70, 0.28);
  }
  * { margin: 0; padding: 0; box-sizing: border-box; }
  html, body { width: 900px; height: 1200px; overflow: hidden; }
  body { background: var(--page-bg); position: relative; font-family: "Arimo", Arial, sans-serif; }

  .card {
    position: absolute;
    left: 87px;
    width: 734px;
    height: 429px;
    border-radius: 24px;
    overflow: hidden;
    box-shadow: 0 8px 22px var(--shadow);
  }
  .card--front { top: 126px; display: flex; background: var(--card-white); }
  .card--back {
    top: 641px;
    background: linear-gradient(90deg, var(--brand-deep) 0%, var(--brand-mid) 50%, var(--brand) 100%);
    display: flex; align-items: center; justify-content: center;
  }

  .front__brand {
    width: 364px; height: 100%;
    background: linear-gradient(90deg, var(--brand-mid), var(--brand));
    display: flex; align-items: center; justify-content: center;
  }
  .front__details { flex: 1; padding: 130px 0 0 47px; }

  .wordmark {
    font-family: "Montserrat", Arial, sans-serif;
    font-weight: 600;
    color: var(--on-brand);
    text-align: center;
    line-height: 1.1;
  }
  .wordmark__name { display: block; }
  .front__brand .wordmark { font-size: 44px; }
  .front__brand .wordmark__sub { font-size: 17px; letter-spacing: 0.5px; display: block; margin-top: 6px; }
  .card--back .wordmark { font-size: 72px; }
  .card--back .wordmark__sub { font-size: 22px; letter-spacing: 0.8px; display: block; margin-top: 8px; }

  .person__name { font-size: 26px; font-weight: 700; color: var(--ink); }
  .person__title { font-size: 17px; color: var(--brand); margin-top: 6px; }

  .contact-list { list-style: none; margin-top: 22px; }
  .contact-list li {
    display: flex; align-items: center; gap: 9px;
    font-size: 16.5px; color: var(--ink);
    height: 25.5px;
  }
  .contact-icon { width: 17px; height: 17px; flex: none; }
</style>
</head>
<body>

<section class="card card--front">
  <div class="front__brand">
    <div class="wordmark">
      <span class="wordmark__name">Meridel</span>
      <span class="wordmark__sub">HEALTH SYSTEMS</span>
    </div>
  </div>
  <div class="front__details">
    <h1 class="person__name">Daniel Avery</h1>
    <p class="person__title">Managing Director</p>
    <ul class="contact-list">
      <li>
        <svg class="contact-icon" viewBox="0 0 17 17"><rect width="17" height="17" rx="3" fill="#6b449b"/><path d="M5 4.2l1.8-.4 1 2.4-1.1.9a6 6 0 0 0 2.8 2.8l.9-1.1 2.4 1-.4 1.8c-4 .4-7.8-3.4-7.4-7.4z" fill="#fff"/></svg>
        084-512-7390
      </li>
      <li>
        <svg class="contact-icon" viewBox="0 0 17 17"><rect width="17" height="17" rx="3" fill="#6b449b"/><path d="M5 4.2l1.8-.4 1 2.4-1.1.9a6 6 0 0 0 2.8 2.8l.9-1.1 2.4 1-.4 1.8c-4 .4-7.8-3.4-7.4-7.4z" fill="#fff"/></svg>
        028-611-2274
      </li>
      <li>
        <svg class="contact-icon" viewBox="0 0 17 17"><rect width="17" height="17" rx="3" fill="#6b449b"/><rect x="3.8" y="5" width="9.4" height="7" fill="none" stroke="#fff" stroke-width="1.2"/><path d="M3.8 5l4.7 3.8L13.2 5" fill="none" stroke="#fff" stroke-width="1.2"/></svg>
        daniel@meridelhealth.com
      </li>
      <li>
        <svg class="contact-icon" viewBox="0 0 17 17"><rect width="17" height="17" rx="3" fill="#6b449b"/><circle cx="8.5" cy="8.5" r="4.6" fill="none" stroke="#fff" stroke-width="1.1"/><ellipse cx="8.5" cy="8.5" rx="2" ry="4.6" fill="none" stroke="#fff" stroke-width="1"/><path d="M3.9 8.5h9.2" stroke="#fff" stroke-width="1"/></svg>
        www.meridelhealth.com
      </li>
    </ul>
  </div>
</section>

<section class="card card--back">
  <div class="wordmark">
    <span class="wordmark__name">Meridel</span>
    <span class="wordmark__sub">HEALTH SYSTEMS</span>
  </div>
</section>

</body>
</html>
```